Redesign of existing business card

I would like the "signage" attachment converted into a business card. This needs to be double sided aswell, keeping the phone number and names on the front, and the email + website on the back.

Second attachment is the current business card design.

Larger font for contact details is required.

Must keep to original color themes (electric blue, silver/grey etc)

Back of the card to have blue background with white writing.

Industry/Entity Type

Business

Contact Information for Business Card

Refer to existing design from attachments

Requirements
Must have
• Refer to existing design from attachments
Nice to have

```html
<!DOCTYPE html>
<html lang="en">
<head>
<meta charset="utf-8">
<title>Kelvar Electro Services – Business Card</title>
<link href="https://fonts.googleapis.com/css2?family=Cinzel:wght@400&family=Saira:ital,wght@0,600;0,700;1,800&display=swap" rel="stylesheet">
<style>
  :root {
    --stage: #000000;
    --electric-blue: #3a55a6;
    --steel-grey: #939598;
    --rule-grey: #8c8d90;
    --silver-light: #ffffff;
    --silver-mid: #e4e5e7;
    --silver-dark: #c9cacc;
    --ring-grey: #d6d7d9;
    --name-grey: #e6e6e6;
    --white: #ffffff;
  }
  * { margin: 0; padding: 0; box-sizing: border-box; }
  html, body {
    width: 1200px; height: 1200px; overflow: hidden;
    background: var(--stage);
  }
  .canvas { position: relative; width: 1200px; height: 1200px; }
  .card {
    position: absolute; left: 175px; width: 850px; height: 520px; overflow: hidden;
  }
  .card--front {
    top: 62px;
    background: linear-gradient(180deg, var(--silver-light) 0%, var(--silver-mid) 100%);
  }
  .card--back { top: 618px; background: var(--electric-blue); }

  .front-shapes { position: absolute; inset: 0; }

  .brand-ring {
    position: absolute; left: 77px; top: 38px; width: 256px; height: 256px;
    border-radius: 50%; border: 22px solid var(--ring-grey);
  }
  .brand-name {
    position: absolute; left: 55px; top: 318px; width: 300px;
    font-family: "Saira", sans-serif; font-weight: 700; font-size: 30px;
    line-height: 1.15; text-align: center; text-transform: uppercase;
    letter-spacing: 1px; color: var(--electric-blue);
  }
  .holder-name {
    position: absolute; left: 560px; top: 182px; width: 250px; text-align: right;
    font-family: "Cinzel", serif; font-weight: 400; font-size: 22px;
    letter-spacing: 0.5px; color: var(--name-grey);
  }
  .phone-band {
    position: absolute; left: 0; top: 432px; width: 850px; height: 88px;
    display: flex; align-items: center; justify-content: center;
    font-family: "Saira", sans-serif; font-style: italic; font-weight: 800;
    font-size: 58px; letter-spacing: 1px; color: var(--electric-blue);
    word-spacing: 16px;
  }
  .website {
    position: absolute; left: 0; top: 244px; width: 850px; text-align: center;
    font-family: "Saira", sans-serif; font-weight: 600; font-size: 27px;
    color: var(--white);
  }
</style>
</head>
<body>
<div class="canvas">
  <section class="card card--front">
    <svg class="front-shapes" width="850" height="520" viewBox="0 0 850 520" aria-hidden="true">
      <defs>
        <linearGradient id="band-silver" x1="0" y1="0" x2="1" y2="0">
          <stop offset="0" stop-color="#d2d3d5"/>
          <stop offset="0.35" stop-color="#eeeff0"/>
          <stop offset="0.7" stop-color="#eeeff0"/>
          <stop offset="1" stop-color="#c3c4c6"/>
        </linearGradient>
      </defs>
      <polygon points="534,0 850,0 850,432 365,432" fill="var(--steel-grey)"/>
      <rect x="0" y="432" width="850" height="88" fill="url(#band-silver)"/>
      <polygon points="0,432 365,432 362,441 0,441" fill="var(--rule-grey)"/>
      <polygon points="365,432 850,432 850,441 362,441" fill="#d8d9db"/>
    </svg>
    <div class="brand-ring" aria-hidden="true"></div>
    <div class="brand-name">Kelvar<br>Electro Services</div>
    <div class="holder-name">Daniel Hartono</div>
    <div class="phone-band">TEL 0400 318 592</div>
  </section>

  <section class="card card--back">
    <div class="website">www.kelvarelectro.com.au</div>
  </section>
</div>
</body>
</html>
```